Hockey Sponsorship Proposal

We are looking for a sponsorship proposal design for an apparel company to supply our hockey camps with jerseys and apparel. We want to use lots of visuals so potential business partners can see the exposure and publicity their company could get by working with us. We would like the primary colors to be red, black and white. We have attached a bunch of images but not all need to be used. We would like to see a mix of images with adult players and youth players where appropriate. Although I have provided a rough outline for the information on the powerpoint the text and images can be displayed however you would like.

Here is a link to some proposals to give you an idea of what we are looking for
https://www.quillrack.co.uk/pin/512604837219056471/

Target Market(s)

Athletic Apparel Companies

Industry/Entity Type

It Company

Requirements
Must have
• Please note this should be suitable for web as the proposal will be emailed. This is NOT for print.
Nice to have
• I would like the first page to have a full image as the backdrop with the text over top if possible.

```html
<!DOCTYPE html>
<html lang="en">
<head>
<meta charset="utf-8">
<title>Welby Hockey – Partnership Proposal</title>
<link href="https://fonts.googleapis.com/css2?family=Montserrat:wght@400;500;600;700&family=Roboto+Slab:wght@400;700;800&family=Open+Sans:wght@400;600;700&display=swap" rel="stylesheet">
<style>
:root{
  --red:#e3262a;
  --black:#262626;
  --slate:#4b4846;
  --slate-dark:#3d3a38;
  --white:#ffffff;
  --ice:#8c8a88;
  --label:#9a9a9a;
  --bg:#e6e6e6;
}
*{box-sizing:border-box;margin:0;padding:0}
html,body{width:1200px;height:1200px;overflow:hidden;background:var(--bg)}
body{position:relative;font-family:"Open Sans",sans-serif;color:var(--white)}
.sheet{position:absolute;width:682px;height:482px;transform:scale(.8);transform-origin:0 0;overflow:hidden;background:var(--slate)}
.sheet-1{left:41px;top:165px}
.sheet-2{left:614px;top:165px}
.sheet-3{left:41px;top:611px}
.sheet-6{left:614px;top:618px}
.page-label{position:absolute;width:546px;text-align:center;font:300 19px "Montserrat",sans-serif;letter-spacing:1px;color:var(--label)}
.deco{position:absolute;inset:0;width:682px;height:482px}
.photo{position:absolute}
.abs{position:absolute}
.page-no{position:absolute;right:24px;bottom:24px;width:18px;height:18px;border:1px solid var(--white);border-radius:50%;font:700 9px "Montserrat",sans-serif;display:flex;align-items:center;justify-content:center}
/* page 1 */
.brand{position:absolute;left:185px;top:22px;display:flex;align-items:center;gap:14px}
.brand-mark{width:58px;height:58px;border-radius:50%;background:var(--black)}
.brand-name{font:800 26px/1.1 "Roboto Slab",serif;color:var(--black);letter-spacing:1px}
.cover-title{left:29px;top:284px;font:400 28px/1.2 "Roboto Slab",serif}
.cover-title strong{display:block;font-weight:700;font-size:25px}
.cover-rfp{left:29px;top:388px;font:italic 400 28px/1.2 "Roboto Slab",serif;color:var(--red)}
.cover-rfp strong{display:block;color:var(--white);font-weight:700;font-size:28px}
.cover-url{left:375px;top:452px;font:400 8px "Montserrat",sans-serif;letter-spacing:4px}
/* headings & bullets */
.heading{font:600 27px "Montserrat",sans-serif}
.bullets{list-style:none;font-size:11px}
.bullets li{position:absolute;white-space:nowrap;display:flex;align-items:center;gap:8px}
.tick{width:10px;height:10px;flex:none}
/* page 3 */
.sub{font:600 15px "Montserrat",sans-serif}
.media-pic{position:absolute;left:31px;width:68px;height:68px;border-radius:50%;border:2px solid var(--red);box-shadow:0 0 0 2px var(--white) inset;background:linear-gradient(135deg,#d9d9d9,#8a8a8a 60%,#5a5a5a)}
.media{position:absolute;left:116px;width:530px;font-size:8.4px;line-height:1.35}
.media-head{color:var(--red);font-weight:600;font-size:9.5px}
.media-src{font-weight:700;font-size:8.3px;margin-bottom:13px}
/* page 6 */
.req-tag{left:32px;top:95px;width:190px;height:22px;background:var(--white);clip-path:polygon(8% 0,100% 0,92% 100%,0 100%);color:var(--black);font:500 14px "Montserrat",sans-serif;padding-left:24px;line-height:22px}
.req-tag b{color:var(--red);font-weight:600}
.req-table{position:absolute;left:29px;top:127px;width:624px;border-collapse:separate;border-spacing:0 3px;font-size:6.6px;color:var(--black)}
.req-table th{background:var(--red);color:var(--white);font:700 8.5px "Montserrat",sans-serif;text-align:left;padding:3px 0 3px 28px;height:16px}
.req-table td{background:var(--white);height:11px;padding:0 0 0 28px}
.req-table tr:nth-child(even) td{background:#b5b3b1}
.req-table .c{text-align:center;padding:0}
.cta{left:29px;top:344px;font:600 16px/1.35 "Montserrat",sans-serif}
.cta em{font-style:normal;color:var(--red);font-weight:400}
.contact-tag{left:0;top:408px;width:128px;height:16px;background:var(--white);clip-path:polygon(0 0,100% 0,92% 100%,0 100%);color:var(--black);font:700 8.5px "Montserrat",sans-serif;padding-left:28px;line-height:16px}
.contact{top:434px;display:flex;align-items:center;gap:6px;font:600 8.5px "Montserrat",sans-serif}
.contact svg{width:12px;height:10px}
.faint-mark{left:364px;top:330px;width:74px;height:74px;border-radius:50%;background:rgba(255,255,255,.1)}
</style>
</head>
<body>

<!-- Page 1 : cover -->
<section class="sheet sheet-1" aria-label="Cover page">
  <div class="photo" role="img" aria-label="Team photo of camp players in jerseys on the ice, greyscale" style="left:0;top:108px;width:682px;height:374px;background:linear-gradient(180deg,#6c6a68,#4a4846 55%,#3a3837)"></div>
  <svg class="deco" viewBox="0 0 682 482" aria-hidden="true">
    <rect x="0" y="0" width="682" height="108" fill="#fff"/>
    <polygon points="0,0 48,0 0,62" fill="#e3262a"/>
    <polygon points="60,0 102,0 0,128 0,76" fill="#262626"/>
    <polygon points="112,0 122,0 0,150 0,138" fill="#262626"/>
    <polygon points="612,0 660,0 576,108 528,108" fill="#e3262a"/>
    <polygon points="670,0 682,0 682,10 606,108 592,108" fill="#e3262a"/>
    <polygon points="682,110 682,482 372,482" fill="#e3262a" opacity=".82"/>
    <polygon points="0,412 0,482 300,482 470,255 420,255" fill="#262626" opacity=".85"/>
    <polygon points="300,410 352,410 298,482 246,482" fill="#e3262a"/>
    <polygon points="682,430 682,482 640,482" fill="#262626"/>
  </svg>
  <div class="brand"><span class="brand-mark"></span><span class="brand-name">DORIAN<br>Welby Hockey</span></div>
  <h1 class="abs cover-title">Uniform and Apparel<strong>Partnership Opportunity</strong></h1>
  <p class="abs cover-rfp">Request for<strong>PROPOSAL</strong></p>
  <p class="abs cover-url">WWW.WELBYHOCKEY.COM</p>
  <span class="page-no">01</span>
</section>
<div class="page-label" style="left:41px;top:566px">PAGE-1</div>

<!-- Page 2 -->
<section class="sheet sheet-2" aria-label="About this opportunity">
  <div class="photo" role="img" aria-label="Camp players and coaches posing on the ice in red and white jerseys" style="left:0;top:185px;width:682px;height:297px;background:linear-gradient(180deg,#575452,#6a6563 45%,#7d7a78)"></div>
  <svg class="deco" viewBox="0 0 682 482" aria-hidden="true">
    <polygon points="0,0 72,0 0,92" fill="#e3262a"/>
    <polygon points="84,0 172,0 0,218 0,108" fill="#262626"/>
    <polygon points="682,292 682,482 520,482" fill="#e3262a" opacity=".85"/>
    <polygon points="682,370 682,482 600,482" fill="#262626"/>
    <polygon points="470,428 502,428 468,472 436,472" fill="#e3262a"/>
    <polygon points="682,476 682,482 0,482 0,476" fill="#3d3a38"/>
  </svg>
  <h2 class="abs heading" style="left:178px;top:28px">ABOUT this Opportunity</h2>
  <ul class="bullets">
    <li style="left:144px;top:81px"><svg class="tick" viewBox="0 0 10 10"><circle cx="5" cy="5" r="4.3" fill="none" stroke="#e3262a"/><path d="M3 5.2l1.5 1.5 2.7-3" fill="none" stroke="#e3262a"/></svg>Dorian Welby is seeking a partner to be his official jersey and apparel supplier.</li>
    <li style="left:120px;top:108px"><svg class="tick" viewBox="0 0 10 10"><circle cx="5" cy="5" r="4.3" fill="none" stroke="#e3262a"/><path d="M3 5.2l1.5 1.5 2.7-3" fill="none" stroke="#e3262a"/></svg>Selected supplier will outfit all participants of Dorian’s PHL and youth hockey camps.</li>
    <li style="left:96px;top:132px"><svg class="tick" viewBox="0 0 10 10"><circle cx="5" cy="5" r="4.3" fill="none" stroke="#e3262a"/><path d="M3 5.2l1.5 1.5 2.7-3" fill="none" stroke="#e3262a"/></svg>Selected supplier will outfit all participants of Dorian’s PHL and youth hockey camps.</li>
  </ul>
  <span class="page-no">02</span>
</section>
<div class="page-label" style="left:614px;top:566px">PAGE-2</div>

<!-- Page 3 -->
<section class="sheet sheet-3" aria-label="About Dorian">
  <svg class="deco" viewBox="0 0 682 482" aria-hidden="true">
    <polygon points="0,0 72,0 0,92" fill="#e3262a"/>
    <polygon points="84,0 130,0 0,165 0,108" fill="#262626"/>
    <polygon points="682,300 682,482 520,482" fill="#e3262a"/>
    <polygon points="682,400 682,482 620,482" fill="#262626"/>
    <polygon points="500,425 548,425 508,472 460,472" fill="#e3262a"/>
    <polygon points="682,472 682,482 0,482 0,472" fill="#262626"/>
  </svg>
  <h2 class="abs sub" style="left:181px;top:26px">ABOUT DORIAN</h2>
  <ul class="bullets" style="font-size:8.4px">
    <li style="left:160px;top:53px;white-space:normal;width:520px;align-items:flex-start"><svg class="tick" viewBox="0 0 10 10"><circle cx="5" cy="5" r="4.3" fill="none" stroke="#e3262a"/><path d="M3 5.2l1.5 1.5 2.7-3" fill="none" stroke="#e3262a"/></svg>Preeminent performance coach for many of the PHL’s biggest superstars including Silas Corwin, Preston Kaye &amp; Alden Marsh.</li>
    <li style="left:135px;top:83px"><svg class="tick" viewBox="0 0 10 10"><circle cx="5" cy="5" r="4.3" fill="none" stroke="#e3262a"/><path d="M3 5.2l1.5 1.5 2.7-3" fill="none" stroke="#e3262a"/></svg>Player Development Consultant for the Lakeport Harriers.</li>
    <li style="left:118px;top:104px"><svg class="tick" viewBox="0 0 10 10"><circle cx="5" cy="5" r="4.3" fill="none" stroke="#e3262a"/><path d="M3 5.2l1.5 1.5 2.7-3" fill="none" stroke="#e3262a"/></svg>Regarded as an innovator and leading expert in uncovering new pathways of performance excellence.</li>
  </ul>
  <h3 class="abs sub" style="left:115px;top:136px">DORIAN in the media :</h3>

  <div class="media-pic" style="top:157px" role="img" aria-label="Photo of a player in action"></div>
  <div class="media" style="top:162px"><p class="media-head">Harriers teammates break down Alden Marsh’ unique shooting</p><p class="media-src">RINKWIRE - OCT 19, 2017</p><p>According to Marsh’ father Glen, much of that unpredictable style can be credited to skills coach <b>Dorian Welby,</b> who’s worked with the...</p></div>

  <div class="media-pic" style="top:236px" role="img" aria-label="Photo of a player and coach"></div>
  <div class="media" style="top:241px"><p class="media-head">From Preston Kaye on down, DORIAN WELBY driven to develop players</p><p class="media-src">THE FORECHECK - MAY 9. 2017</p><p>Performance coach Dorian Welby is known best for the work he’s done with some of the PHL’s biggest stars of today. From Silas<br>Corwin to</p></div>

  <div class="media-pic" style="top:313px" role="img" aria-label="Photo of the coach at a rink"></div>
  <div class="media" style="top:319px;width:340px"><p class="media-head" style="width:530px">Harriers skills development coach DORIAN WELBY part of new philosophy</p><p class="media-src">BLUE LINE NOTES - MAY 25, 2015</p><p>As the Harriers rebuild gets underway, the team’s newest skill development coach is just getting started. I had the chance to chat with Dorian Welby</p></div>

  <div class="media-pic" style="top:391px" role="img" aria-label="Photo of skaters training on the ice"></div>
  <div class="media" style="top:397px;width:320px"><p class="media-head" style="width:530px">PHL star players descend on Harbor Ice Arena to train with Bayview</p><p class="media-src">THE COASTAL LEDGER - SEP 4, 2017</p><p>For 25 years, Dorian Welby has been fascinated with the science of hockey. From replaying grainy tapes of Saturday Night Hockey games to</p></div>
  <span class="page-no">03</span>
</section>
<div class="page-label" style="left:41px;top:1015px">PAGE-3</div>

<!-- Page 6 -->
<section class="sheet sheet-6" aria-label="Service requirements and contact">
  <div class="photo" role="img" aria-label="Players skating during a camp session, dimmed" style="left:0;top:0;width:682px;height:482px;background:linear-gradient(180deg,#4e4b49,#474442 60%,#403d3b)"></div>
  <svg class="deco" viewBox="0 0 682 482" aria-hidden="true">
    <polygon points="682,310 682,482 510,482" fill="#e3262a"/>
    <polygon points="682,390 682,482 600,482" fill="#262626"/>
    <polygon points="420,482 560,340 600,340 460,482" fill="#262626"/>
    <polygon points="496,428 530,428 490,472 456,472" fill="#e3262a"/>
    <polygon points="40,94 48,94 30,118 22,118" fill="#e3262a"/>
    <polygon points="215,94 225,94 207,118 197,118" fill="#e3262a"/>
  </svg>
  <div class="abs req-tag"><b>Service</b> Requirements</div>
  <table class="req-table">
    <thead><tr><th style="width:130px">EVENT</th><th style="width:260px">ITEM</th><th class="c" style="width:100px;padding:0;text-align:center">PIECES</th><th style="text-align:center;padding:0">TIMELINE</th></tr></thead>
    <tbody>
      <tr><td>PHL Camp</td><td>Uniform (jersey/sock/pant shell)</td><td class="c">50</td><td class="c">Summer 2018</td></tr>
      <tr><td>PHL Camp</td><td>Apparel (some of t-shirt, shorts, hoodie, track suit, hat, toque)</td><td class="c">50</td><td class="c">Summer 2018</td></tr>
      <tr><td>Welby Super 64</td><td>Uniform (jersey/sock/pant shell)</td><td class="c">400</td><td class="c">Spring 2018</td></tr>
      <tr><td>Welby Super 64</td><td>Apparel (some of t-shirt, shorts, hoodie, track suit, hat, toque)</td><td class="c">400</td><td class="c">Spring 2018</td></tr>
      <tr><td>Welby Festival</td><td>Uniform (jersey/sock/pant shell)</td><td class="c">400</td><td class="c">Spring 2018</td></tr>
      <tr><td>Welby Festival</td><td>Apparel (some of t-shirt, shorts, hoodie, track suit, hat, toque)</td><td class="c">400</td><td class="c">Spring 2018</td></tr>
      <tr><td>Travel Team</td><td>Uniform (jersey/sock/pant shell)</td><td class="c">20</td><td class="c">Fall 2018</td></tr>
    </tbody>
  </table>
  <span class="abs faint-mark"></span>
  <p class="abs cta">If you are <em>INTERESTED IN PARTNERING</em><br>with <em>DORIAN</em> on this opportunity</p>
  <div class="abs contact-tag">PLEASE CONTACT</div>
  <div class="abs contact" style="left:28px"><svg viewBox="0 0 12 10"><circle cx="6" cy="3" r="2.4" fill="#e3262a"/><path d="M1 10c0-3 2-4.5 5-4.5s5 1.5 5 4.5z" fill="#e3262a"/></svg>MARTIN HALE</div>
  <div class="abs contact" style="left:122px"><svg viewBox="0 0 12 10"><path d="M2 1l2 0 1 2.5-1.3 1a6 6 0 0 0 3 3l1-1.3L10 7v2c-5 0-8-3-8-8z" fill="#e3262a"/></svg>555.014.2270</div>
  <div class="abs contact" style="left:226px"><svg viewBox="0 0 12 10"><rect x=".8" y="1.3" width="10.4" height="7.4" fill="none" stroke="#e3262a"/><path d="M1 1.5l5 4 5-4" fill="none" stroke="#e3262a"/></svg>martin.hale@welbyhockey.com</div>
  <span class="page-no">06</span>
</section>
<div class="page-label" style="left:614px;top:1015px">PAGE-6</div>

</body>
</html>
```